New business card with our logo

we finalized our logo with the help of pixel harbor - now we need a business card using that logo. we are a metal service center providing raw steel and metal products for fabricating, contractors, artists, etc. we have the wording for the back of the card figured out (attached, no deviations from text please), just need help putting it all together.
would like the look of steel somehow incorporated in the design ... would like the black part of the logo to be steel or silver color (the S & BRANLEY)
Other font styles liked:
- calibri, arial, similar to those, modern looking
Colors
Designer to choose colors to be used in the design.
Requirements
Must have
- Back of card must haves are attached (no deviations from wording please).
- FRONT of card:
- logo
- address
- name
- office tel
- cell
- fax
- website
- address
Nice to have
- incorporate the look of steel or element of steel somehow
- names of the staff on front not in all caps, i.e. Rosvita not ROSVITA
- this industry is more industrial, not coffee or flower shop so design should be aligned with that
- design should be classic and tasteful

```html
<!DOCTYPE html>
<html lang="en">
<head>
<meta charset="utf-8">
<title>Branley Steel – Business Card</title>
<link rel="stylesheet" href="https://fonts.googleapis.com/css2?family=Roboto:wght@400;500;700&display=swap">
<style>
  :root {
    --backdrop: #6e4f38;
    --card-top: #38383b;
    --card-bottom: #19191b;
    --brand-blue: #1f78c1;
    --steel-light: #e4e6e8;
    --text-light: #eeeeee;
    --text-muted: #c9c9c9;
    --rule: #3f6f99;
  }
  * { box-sizing: border-box; margin: 0; padding: 0; }
  html, body { width: 1200px; height: 960px; overflow: hidden; }
  body {
    background: var(--backdrop);
    font-family: "Roboto", Arial, sans-serif;
    position: relative;
  }
  .card {
    position: absolute;
    left: 322px;
    width: 600px;
    height: 344px;
    border-radius: 18px;
    overflow: hidden;
    background:
      repeating-linear-gradient(90deg, rgba(255,255,255,0.025) 0 1px, transparent 1px 3px),
      linear-gradient(180deg, var(--card-top), var(--card-bottom));
    box-shadow: 0 4px 10px rgba(0,0,0,0.45);
  }
  .card--front { top: 108px; }
  .card--back { top: 493px; }

  .brand {
    position: absolute;
    display: flex;
    align-items: center;
    gap: 14px;
  }
  .brand__circle {
    border: 5px solid var(--brand-blue);
    border-radius: 50%;
  }
  .brand__name {
    color: var(--steel-light);
    font-weight: 700;
    letter-spacing: 0.5px;
    white-space: nowrap;
  }
  .card--front .brand { right: 28px; top: 38px; }
  .card--front .brand__circle { width: 66px; height: 66px; }
  .card--front .brand__name { font-size: 31px; }

  .person { position: absolute; left: 28px; top: 163px; }
  .person__name { color: var(--brand-blue); font-size: 20px; font-weight: 700; }
  .person__title { color: var(--text-muted); font-size: 15px; margin-top: 2px; }

  .divider {
    position: absolute; left: 28px; right: 30px; top: 215px;
    height: 1px; background: var(--rule);
  }

  .contacts { position: absolute; left: 28px; top: 226px; list-style: none; }
  .contacts li {
    display: flex; align-items: center; gap: 8px;
    color: var(--text-light); font-size: 14px; height: 19px;
  }
  .contacts svg { width: 14px; height: 14px; fill: var(--brand-blue); }

  .address {
    position: absolute; right: 29px; top: 265px;
    text-align: right; color: var(--text-light); font-size: 14px; line-height: 19px;
  }

  .footer-band {
    position: absolute; left: 0; bottom: 0;
    width: 600px; height: 22px;
    background: var(--brand-blue);
    display: flex; align-items: center; justify-content: flex-end;
    padding-right: 30px;
  }
  .website {
    color: #ffffff; font-size: 14px; letter-spacing: 2.4px;
  }

  .card--back .brand { left: 50%; top: 50%; transform: translate(-50%, -50%); gap: 20px; }
  .card--back .brand__circle { width: 130px; height: 130px; border-width: 9px; }
  .card--back .brand__name { font-size: 34px; }
</style>
</head>
<body>

<section class="card card--front" aria-label="Business card front">
  <div class="brand">
    <span class="brand__circle"></span>
    <span class="brand__name">BRANLEY STEEL</span>
  </div>

  <div class="person">
    <p class="person__name">DANA WHITLOCK</p>
    <p class="person__title">CEO/FOUNDER</p>
  </div>

  <div class="divider"></div>

  <ul class="contacts">
    <li>
      <svg viewBox="0 0 24 24" aria-hidden="true"><path d="M6.6 10.8a15 15 0 0 0 6.6 6.6l2.2-2.2c.3-.3.7-.4 1-.2 1.1.4 2.3.6 3.6.6.6 0 1 .4 1 1V20c0 .6-.4 1-1 1A17 17 0 0 1 3 4c0-.6.4-1 1-1h3.5c.6 0 1 .4 1 1 0 1.3.2 2.5.6 3.6.1.3 0 .7-.2 1z"/></svg>
      555 214 7730
    </li>
    <li>
      <svg viewBox="0 0 24 24" aria-hidden="true"><path d="M7 1h10a2 2 0 0 1 2 2v18a2 2 0 0 1-2 2H7a2 2 0 0 1-2-2V3a2 2 0 0 1 2-2zm0 3v14h10V4zm5 15.5a1.2 1.2 0 1 0 0 2.4 1.2 1.2 0 0 0 0-2.4z"/></svg>
      555 382 6091
    </li>
    <li>
      <svg viewBox="0 0 24 24" aria-hidden="true"><path d="M6 2h12v6H6zM3 9h18a2 2 0 0 1 2 2v7h-4v4H5v-4H1v-7a2 2 0 0 1 2-2zm4 7v4h10v-4z"/></svg>
      555 907 4418
    </li>
    <li>
      <svg viewBox="0 0 24 24" aria-hidden="true"><path d="M2 5h20v2l-10 6L2 7zm0 4.3l10 6 10-6V19H2z"/></svg>
      dana@branleysteel.com
    </li>
  </ul>

  <p class="address">1240 Foundry Road<br>Millbrook, Ohio 44820</p>

  <div class="footer-band">
    <p class="website">www.branleysteel.com</p>
  </div>
</section>

<section class="card card--back" aria-label="Business card back">
  <div class="brand">
    <span class="brand__circle"></span>
    <span class="brand__name">BRANLEY STEEL</span>
  </div>
</section>

</body>
</html>
```